Airplane Billboard

This is a banner that will flown behind an airplane up 1000 ft in the air.

The size of the banner will be 25 feet high x 60 feet wide.

I'd like our logo to cover 25 feet x 25 feet- to the left side of the banner.

Then I would like the text to read : Bachelor Party Headquarters
Franklin, WI www.kvm.place

Target Market(s)

males 21-45

Font styles to use
Sans Serif

Colors

Designer to choose colors to be used in the design.

Requirements
Must have
• Our logo. I tried to attach the high resolution logo but it was too large.
• The text: Bachelor Party Headquarters
• Our location: Franklin,WI
• Our web site: www.kvm.place

```html
<!DOCTYPE html>
<html lang="en">
<head>
<meta charset="utf-8">
<title>KVM – Bachelor Party Headquarters</title>
<link rel="stylesheet" href="https://fonts.googleapis.com/css2?family=Jost:wght@500&family=Roboto+Condensed:wght@700&family=Nunito:wght@900&display=swap">
<style>
  :root {
    --frame: #2b2b2d;
    --ink: #0b0b0b;
    --white: #ffffff;
    --mist: #f2f2f4;
    --silver: #dcdce2;
    --pink: #e98ee6;
    --magenta: #c24fc9;
    --violet: #8a4cc7;
    --sky: #6fb0ee;
    --plum: #3a1c4e;
    --haze: rgba(60, 40, 70, 0.16);
  }
  html, body {
    margin: 0;
    padding: 0;
    width: 1200px;
    height: 514px;
    overflow: hidden;
    background: var(--frame);
  }
  .banner {
    position: relative;
    width: 1200px;
    height: 514px;
    box-sizing: border-box;
    border: 8px solid var(--frame);
    overflow: hidden;
    background:
      linear-gradient(180deg,
        var(--mist) 0%,
        var(--silver) 38%,
        var(--pink) 62%,
        var(--magenta) 80%,
        var(--violet) 100%);
  }
  .banner__glow {
    position: absolute;
    inset: 0;
    background:
      radial-gradient(ellipse 420px 160px at 860px 470px, rgba(111,176,238,0.75), transparent 70%),
      radial-gradient(ellipse 300px 120px at 1150px 500px, rgba(58,28,78,0.8), transparent 70%);
  }
  .banner__performers {
    position: absolute;
    left: 500px;
    top: 0;
    right: 0;
    bottom: 0;
    background: linear-gradient(90deg, transparent 0%, var(--haze) 25%, var(--haze) 75%, transparent 100%);
  }
  .brand {
    position: absolute;
    left: 30px;
    top: 0;
    width: 500px;
    margin: 0;
    color: var(--ink);
    font-family: "Jost", sans-serif;
    font-weight: 500;
    line-height: 1;
  }
  .brand__mark {
    position: absolute;
    left: 0;
    top: 48px;
    font-size: 240px;
    letter-spacing: -4px;
    line-height: 1;
    white-space: nowrap;
  }
  .brand__name {
    position: absolute;
    left: 2px;
    top: 346px;
    font-size: 46px;
    letter-spacing: 1px;
    text-transform: uppercase;
    white-space: nowrap;
  }
  .tagline {
    position: absolute;
    left: 694px;
    top: 84px;
    margin: 0;
    color: var(--ink);
    font-family: "Roboto Condensed", sans-serif;
    font-weight: 700;
    line-height: 1;
    white-space: nowrap;
    text-shadow: 0 0 3px var(--white), 0 0 3px var(--white), 0 0 5px var(--white);
  }
  .tagline__headline {
    display: block;
    font-size: 40px;
    letter-spacing: -0.8px;
  }
  .tagline__location {
    display: block;
    margin-top: 6px;
    font-size: 64px;
    letter-spacing: -2px;
  }
  .web-address {
    position: absolute;
    left: 680px;
    top: 368px;
    margin: 0;
    color: var(--ink);
    font-family: "Nunito", sans-serif;
    font-weight: 900;
    font-size: 50px;
    line-height: 1;
    white-space: nowrap;
    text-shadow: 0 0 3px var(--white), 0 0 3px var(--white), 0 0 4px var(--white), 0 0 6px var(--white);
  }
</style>
</head>
<body>
  <main class="banner">
    <div class="banner__glow"></div>
    <div class="banner__performers" role="img" aria-label="Photo area: silhouettes of two pole dancers performing on poles"></div>

    <h1 class="brand">
      <span class="brand__mark">KVM</span>
      <span class="brand__name">Kestrel Valley Mill</span>
    </h1>

    <p class="tagline">
      <span class="tagline__headline">Bachelor Party Headquarters</span>
      <span class="tagline__location">Franklin,WI</span>
    </p>

    <p class="web-address">www.kvm.place</p>
  </main>
</body>
</html>
```